Coinvale Landing Page | A free, personalized stock market email

We are looking for someone to revamp our landing page at https://coinvale-example.com . You should get to know the product and what it offers, and present new designs for our landing page. Feel free to use assets that currently exist on the page, as well as any new assets that you can put together. This landing page should make it obvious what the product does and aim to dramatically increase our conversion rate. We are looking for creativity, uniqueness, and clarity of purpose.

Target Market(s)

People who are invested in, or interested in being invested in, the stock market

Industry/Entity Type

Finance

Number of Pages Required

1 page

Font styles to use
Sans Serif

Requirements
Must have
• Creativity, sleek/minimal design, existing color palette and logos
Nice to have
• Effective copy
Should not have
• Clutter

```html
<!DOCTYPE html>
<html lang="en">
<head>
<meta charset="utf-8">
<title>Coinvale — Do Less, Know More</title>
<link href="https://fonts.googleapis.com/css2?family=Poppins:wght@400;500;600;700;800&family=Inter:wght@400;500;600;700&display=swap" rel="stylesheet">
<style>
:root{
  --blue:#0a6db5;
  --blue-bright:#0b78c6;
  --ink:#14171c;
  --band:#d6eaf7;
  --box:#dfeffa;
  --green:#6ccb6c;
  --toggle-off:#d5d7da;
  --arc:#dcefd9;
  --footer:#efefef;
  --muted:#6b7075;
  --white:#ffffff;
}
*{margin:0;padding:0;box-sizing:border-box}
html,body{width:1200px;height:2487px;overflow:hidden;background:var(--white)}
body{position:relative;font-family:'Poppins',sans-serif;color:var(--ink)}
.abs{position:absolute}
a{color:inherit}

/* brand */
.brand{display:flex;align-items:center;gap:8px;font-weight:500;color:var(--blue)}
.brand-dot{width:.7em;height:.7em;border-radius:50%;background:var(--blue)}

/* header */
.signin{left:1048px;top:13px;width:103px;height:30px;border-radius:15px;background:var(--blue);color:var(--white);font-size:16px;display:flex;align-items:center;justify-content:center;text-decoration:none}
.top-brand{left:0;width:1200px;top:30px;justify-content:center;font-size:38px}
.corner{width:0;height:0}
.corner-tl{left:0;top:75px;border-top:105px solid var(--blue);border-right:105px solid transparent}
.corner-br{right:0;top:378px;border-bottom:104px solid var(--blue);border-left:104px solid transparent}

/* hero */
.hero-mark{left:322px;top:150px;width:126px;height:155px;border-radius:50%;background:linear-gradient(160deg,#11c6e6,#0a6db5)}
.hero-title{left:495px;top:146px;font-size:61px;font-weight:700;line-height:76px;letter-spacing:-.5px}
.hero-title .accent{color:var(--blue-bright)}
.bracket{left:665px;top:307px;width:54px;height:112px;border:2px solid var(--blue);border-left:none}
.btn-primary{left:495px;top:339px;width:210px;height:52px;border-radius:6px;background:var(--blue);color:var(--white);font-size:19px;font-weight:500;display:flex;align-items:center;justify-content:center;text-decoration:none}
.sample-link{left:0;width:1200px;top:431px;text-align:center;font-size:13.5px;font-weight:500}
.sample-link a{text-decoration:underline;text-underline-offset:4px}

/* steps band */
.band{left:0;top:482px;width:1200px;height:472px;background:var(--band)}
.card{background:var(--white);box-shadow:0 1px 6px rgba(0,0,0,.18);font-family:'Inter',sans-serif;overflow:hidden}
.card-head{height:38px;border-bottom:1px solid #e6e6e6;display:flex;align-items:center;justify-content:center;position:relative;font-size:13px}
.card-head .back{position:absolute;left:14px;font-size:14px}
.card-head .brand{font-family:'Poppins',sans-serif;font-size:13px;gap:4px}
.step-1{left:165px;top:519px;width:256px;height:541px}
.step-2{left:476px;top:519px;width:261px;height:541px}
.step-3{left:792px;top:519px;width:256px;height:541px}
.card-body{padding:24px 24px 0 29px}
.card h3{font-family:'Poppins',sans-serif;font-size:18px;font-weight:700;line-height:21px}
.step-1 h3{font-size:17px}
.row{display:flex;justify-content:space-between;align-items:center;font-size:10px;border-bottom:1px solid #dcdcdc;height:40px}
.toggle{width:22px;height:11px;border-radius:6px;background:var(--green);position:relative;flex:none}
.toggle::after{content:"";position:absolute;top:2px;right:2px;width:7px;height:7px;border-radius:50%;background:var(--white)}
.toggle.off{background:var(--toggle-off)}
.toggle.off::after{right:auto;left:2px}
.label-sm{font-size:10px;font-weight:600;color:#777;margin-top:20px}
.note{font-size:7px;color:#333;margin:4px 0 6px}
.link-u{text-decoration:underline}
.sched .row{height:37.5px}
.step-caption{width:300px;text-align:center;font-size:18px;font-weight:600;line-height:26px}

/* email card */
.mail-brand{justify-content:center;font-size:25px;margin-top:8px}
.mail-date{text-align:center;font-size:9px;margin-top:16px}
.stock{margin:22px 10px 0;border:1px solid #e5e5e5;border-radius:6px;padding:12px 11px 0}
.ticker{display:flex;align-items:center;gap:7px}
.ticker b{font-size:15px;color:var(--blue);font-weight:700}
.price{background:#eee;border-radius:9px;font-size:11px;font-weight:700;padding:2px 7px}
.tiny{font-size:7px}
.changes{display:flex;gap:14px;margin:8px 0 8px 2px;font-size:9px;font-weight:700}
.changes small{display:block;font-size:6px;font-weight:400}
.sect{font-size:7.5px;color:#b9b9b9;border-top:1px solid #e5e5e5;padding-top:6px}
.rating{display:flex;align-items:center;gap:12px;margin:12px 0 14px 5px}
.buy{width:42px;height:40px;background:#9ee09c;border-radius:3px;font-size:10px;font-weight:600;color:#3c7a3c;display:flex;align-items:center;justify-content:center}
.bars{width:82px;display:flex;flex-direction:column;gap:6px}
.bars i{display:block;height:3px;background:var(--green);border-radius:2px}
.pcts{font-size:8px;line-height:12px;color:#777}
.ind{margin:10px 9px 12px;font-size:8.5px}
.ind div{display:flex;border-bottom:1px solid #aaa;padding-bottom:3px;font-weight:600}
.ind p{display:flex;padding-top:5px}
.ind span{width:88px}
.news{margin:10px 6px 14px;background:#eef1f4;border-radius:4px;display:flex;gap:8px;padding:6px}
.thumb{width:40px;height:36px;background:linear-gradient(135deg,#5a6470,#b89a86);flex:none}
.news b{font-size:8.5px;line-height:11px;display:block}
.news small{font-size:6.5px;color:#999;line-height:8px;display:block;margin-top:3px}

/* benefits */
.big-mark{left:21px;top:1312px;width:354px;height:478px;border-radius:50%;background:linear-gradient(160deg,#0fd6e6,#0a6db5 60%)}
.timeline{left:0;top:0;width:1200px;height:2100px}
.sketch{background:linear-gradient(180deg,#f1f2f3,#e2e4e6)}
.benefit{background:var(--box);border-radius:10px}
.benefit h2{font-size:27px;font-weight:600;line-height:39px;color:#262a2f;white-space:nowrap}
.benefit h2 .accent{color:var(--blue-bright)}
.benefit p{font-size:16px;line-height:24px;color:#363a3f;margin-top:8px}
.benefit .strong{font-weight:600;color:var(--ink);margin-top:12px;font-size:16px}
.b1{left:574px;top:1215px;width:487px;height:156px;padding:22px 30px 22px 54px}
.b2{left:664px;top:1408px;width:487px;height:194px;padding:16px 30px 16px 54px}
.b3{left:664px;top:1640px;width:487px;height:176px;padding:18px 28px 18px 48px}
.b4{left:574px;top:1858px;width:487px;height:176px;padding:16px 40px 16px 60px}

/* closing band */
.cta-band{left:0;top:2105px;width:1200px;height:272px;background:var(--blue);color:var(--white);text-align:center}
.cta-band .brand{color:var(--white);justify-content:center;font-size:40px;margin-top:24px}
.cta-band .brand-dot{background:var(--white)}
.cta-title{font-size:35px;font-weight:700;margin-top:22px;letter-spacing:-.3px}
.btn-light{display:inline-flex;align-items:center;justify-content:center;width:182px;height:42px;border-radius:5px;background:var(--white);color:#222;font-size:16px;margin-top:20px;text-decoration:none}
.cta-link{font-size:13px;font-weight:600;margin-top:12px}
.cta-link a{text-decoration:underline;text-underline-offset:3px}

.site-footer{left:0;top:2377px;width:1200px;height:110px;background:var(--footer);color:var(--muted);font-size:16px}
.copyright{left:75px;top:43px}
.social{left:582px;top:44px;display:flex;gap:14px}
.social span{width:20px;height:20px;border-radius:50%;background:#c7202a}
.social span:first-child{background:#1b1b1b}
.footer-links{right:50px;top:42px;display:flex;gap:30px;color:#333}
.footer-links li{list-style:none;display:flex;align-items:center;gap:6px}
.footer-links li::before{content:"";width:7px;height:7px;border-radius:50%;background:var(--blue-bright)}
</style>
</head>
<body>

<header>
  <a class="abs signin" href="https://coinvale-example.com">Sign in</a>
  <div class="abs brand top-brand"><span class="brand-dot"></span>Coinvale</div>
</header>

<div class="abs corner corner-tl"></div>
<div class="abs corner corner-br"></div>

<section class="hero">
  <div class="abs hero-mark" aria-hidden="true"></div>
  <h1 class="abs hero-title"><span class="accent">DO</span> LESS<br><span class="accent">KNOW</span> MORE</h1>
  <div class="abs bracket"></div>
  <a class="abs btn-primary" href="https://coinvale-example.com">Sign Up For Free</a>
  <p class="abs sample-link"><a href="https://coinvale-example.com">See a Full Email Sample</a></p>
</section>

<section class="steps">
  <div class="abs band"></div>

  <div class="abs card step-1">
    <div class="card-head"><span class="back">←</span><span class="brand"><span class="brand-dot"></span>Coinvale</span></div>
    <div class="card-body">
      <h3>Novatech Corporation<br>(NVTK)</h3>
      <div class="row" style="height:56px;margin-top:6px;border-bottom:1px solid #bbb"><span style="display:flex;gap:10px;align-items:center">Toggle All <span class="toggle"></span></span></div>
      <p class="label-sm">Data</p>
      <p class="note">This data is always delivered.</p>
      <div class="row"><span>Price</span><span class="toggle"></span></div>
      <div class="row"><span>News</span><span class="toggle"></span></div>
      <div class="row"><span>Analyst Ratings</span><span class="toggle"></span></div>
      <p class="label-sm">Indicators</p>
      <p class="note">Indicator data is only delivered when the indicator is triggered.</p>
      <div class="row"><span class="link-u">Bollinger Bands</span><span class="toggle"></span></div>
      <div class="row"><span class="link-u">MACD</span><span class="toggle"></span></div>
      <div class="row"><span class="link-u">Relative Strength Index</span><span class="toggle"></span></div>
    </div>
  </div>

  <div class="abs card step-2">
    <div class="card-head"><span class="back">←</span><span class="brand"><span class="brand-dot"></span>Coinvale</span></div>
    <div class="card-body sched" style="padding-left:33px;padding-right:30px">
      <h3>Your Schedule</h3>
      <p style="font-size:9.5px;line-height:17px;margin-top:10px">Currently, we only offer notifications during market trading hours.</p>
      <p style="font-size:9.5px;margin-top:8px">Your timezone is: <b>America/New_York</b></p>
      <p style="font-size:7px;margin:10px 0 4px" class="link-u">Change timezone</p>
      <div style="border-top:1px solid #bbb"></div>
      <div class="row"><span>9:30 AM</span><span class="toggle"></span></div>
      <div class="row"><span>10:00 AM</span><span class="toggle off"></span></div>
      <div class="row"><span>10:30 AM</span><span class="toggle"></span></div>
      <div class="row"><span>11:00 AM</span><span class="toggle off"></span></div>
      <div class="row"><span>11:30 AM</span><span class="toggle off"></span></div>
      <div class="row"><span>12:00 PM</span><span class="toggle off"></span></div>
      <div class="row"><span>12:30 PM</span><span class="toggle"></span></div>
      <div class="row"><span>1:00 PM</span><span class="toggle off"></span></div>
      <div class="row"><span>1:30 PM</span><span class="toggle off"></span></div>
    </div>
  </div>

  <div class="abs card step-3">
    <div class="brand mail-brand"><span class="brand-dot"></span>Coinvale</div>
    <p class="mail-date">4:30 PM, June 02 2023</p>
    <div class="stock">
      <div class="ticker"><b>NVTK</b><span class="price">$393.27</span></div>
      <p class="tiny" style="margin-top:4px">Novatech Corporation</p>
      <div class="changes">
        <span style="color:#111">▾ −1.11%<small>1-Day</small></span>
        <span>▴ +39.41%<small>30-Day</small></span>
        <span>▴ +100.92%<small>1-Year</small></span>
      </div>
      <p class="sect">ANALYST RATINGS</p>
      <p style="font-size:9px;margin:6px 0 0 5px">What 41 Wallstreet experts are saying:</p>
      <div class="rating">
        <div class="buy">BUY</div>
        <div class="bars"><i style="width:100%"></i><i style="width:14%;background:#ddd"></i><i style="width:3%;background:#ddd"></i></div>
        <div class="pcts">85.4%&nbsp;&nbsp;Buy<br>12.2%&nbsp;&nbsp;Hold<br>2.4%&nbsp;&nbsp;&nbsp;&nbsp;Sell</div>
      </div>
      <p class="sect">INDICATORS</p>
      <div class="ind"><div><span>Signal</span>Type</div><p><span>Bollinger Bands</span>BUY</p></div>
      <p class="sect">NEWS</p>
      <div class="news">
        <div class="thumb" role="img" aria-label="News video thumbnail"></div>
        <div><b>Dana Holt on Novatech, AI Investments and US Economy</b><small>By staff via Marketline Markets and Finance</small></div>
      </div>
    </div>
    <div class="stock" style="margin-top:14px;padding-bottom:12px">
      <div class="ticker"><b>JPR</b><span class="price">$140.47</span></div>
    </div>
  </div>

  <p class="abs step-caption" style="left:143px;top:1080px">Subscribe To<br>Accet Notification</p>
  <p class="abs step-caption" style="left:449px;top:1080px">Set Your Schedule</p>
  <p class="abs step-caption" style="left:776px;top:1080px">Get Your Email</p>
</section>

<section class="benefits">
  <div class="abs big-mark" aria-hidden="true"></div>
  <svg class="abs timeline" viewBox="0 0 1200 2100" aria-hidden="true">
    <path d="M282 1228 C470 1420 470 1800 225 1975" fill="none" stroke="var(--arc)" stroke-width="9" stroke-linecap="round"/>
    <circle cx="336" cy="1288" r="15" fill="var(--blue)"/>
    <circle cx="414" cy="1472" r="15" fill="var(--blue)"/>
    <circle cx="413" cy="1692" r="15" fill="var(--blue)"/>
    <circle cx="314" cy="1891" r="15" fill="var(--blue)"/>
  </svg>

  <div class="abs sketch" style="left:436px;top:1205px;width:90px;height:158px" role="img" aria-label="Sketch of a man in a suit waving"></div>
  <div class="abs sketch" style="left:436px;top:1390px;width:215px;height:130px" role="img" aria-label="Sketch of a man relaxing in a beach chair under the sun"></div>
  <div class="abs sketch" style="left:436px;top:1605px;width:222px;height:165px" role="img" aria-label="Sketch of a man receiving a flying letter"></div>
  <div class="abs sketch" style="left:248px;top:1800px;width:322px;height:190px" role="img" aria-label="Sketch of a man chasing stock tickers with a butterfly net in a field"></div>

  <div class="abs benefit b1"><h2><span class="accent">Coinvale</span> is your free,<br>personalized, data-driven<br>finance email</h2></div>
  <div class="abs benefit b2"><h2>Stop scanning charts and<br>chasing data</h2><p>Don't bend over backwards to get the investment insights you need. You have better ways to spend your time and energy.</p></div>
  <div class="abs benefit b3"><h2>Let the information come<br>right to you</h2><p>We'll send you curated market insights exactly when you want them</p></div>
  <div class="abs benefit b4"><h2>Stop paying for information</h2><p>Don't spend a dime on financial information, use that money for investments</p><p class="strong">Coinvale is free. Period</p></div>
</section>

<section class="abs cta-band">
  <div class="brand"><span class="brand-dot"></span>Coinvale</div>
  <h2 class="cta-title">DO LESS, KNOW MORE TODAY</h2>
  <a class="btn-light" href="https://coinvale-example.com">Sign Up For Free</a>
  <p class="cta-link"><a href="https://coinvale-example.com">See a Full Email Sample</a></p>
</section>

<footer class="abs site-footer">
  <p class="abs copyright">Copyright © 2023 Coinvale</p>
  <div class="abs social" aria-label="Social channels"><span></span><span></span></div>
  <ul class="abs footer-links"><li>Blog</li><li>Terms of use</li><li>Privacy Policy</li></ul>
</footer>

</body>
</html>
```